Exciting & Elegant Stationary Pack

Stationary consists of
1. Letter head / Envelope
2. Business Card
3. Invoice
4. 40x40mm sticker

Attached files;

1. Logo (Other formats available on request)
2. MS word Doc - For information and description of design
3. Website image (This will be our new website so use the colours so everything ties together)
4. Sample of stationary pack we like, but feel free to be creative

Target Market(s)

Home improvement

Industry/Entity Type

Construction

Font styles to use
Other font styles liked:
• Leave up to designer - We like font used on (website attached image)

Requirements
Must have
• Please look at uploaded file of sample website and use colours
Nice to have
• Any type of business card design - eg. metal, die cut, embossed, etc...

```html
<!DOCTYPE html>
<html lang="en">
<head>
<meta charset="utf-8">
<title>Tessera Tiling Stationery</title>
<link rel="stylesheet" href="https://fonts.googleapis.com/css2?family=Montserrat:wght@500;700;800&family=Tinos&display=swap">
<style>
  :root {
    --navy: #123f66;
    --mist: #c9d5df;
    --paper: #ffffff;
    --backdrop: #e7e8e9;
    --ink: #1c1c1c;
  }
  * { box-sizing: border-box; margin: 0; padding: 0; }
  html, body { width: 1200px; height: 775px; overflow: hidden; }
  body { background: var(--backdrop); font-family: "Montserrat", sans-serif; position: relative; }
  .sheet { position: absolute; background: var(--paper); box-shadow: 0 2px 6px rgba(0,0,0,.12); overflow: hidden; }

  .brand { font-family: "Montserrat", sans-serif; font-weight: 800; color: var(--navy); letter-spacing: .02em; line-height: 1; }
  .brand-faint { color: var(--mist); }

  /* Letterhead */
  .letterhead { left: 64px; top: 35px; width: 500px; height: 712px; }
  .letterhead .brand-main { position: absolute; left: 40px; top: 48px; font-size: 34px; }
  .header-band { position: absolute; left: 150px; top: 98px; width: 140px; height: 24px; background: var(--navy); }
  .company-title { position: absolute; right: 18px; top: 84px; text-align: right; color: var(--navy); font-weight: 700; }
  .company-title .name { font-size: 16px; }
  .company-title .abn { font-size: 14px; margin-top: 2px; }
  .letter-body { position: absolute; left: 40px; top: 170px; width: 420px; font-family: "Tinos", serif; font-size: 12.5px; line-height: 1.2; color: var(--ink); }
  .letter-body p { margin-bottom: 13px; }
  .letter-body .signoff { margin-top: 26px; }
  .contact-block { position: absolute; display: flex; align-items: flex-start; gap: 10px; }
  .contact-block .marker { width: 30px; height: 40px; background: var(--navy); }
  .contact-block ul { list-style: none; color: var(--navy); font-weight: 700; font-size: 10px; line-height: 1.45; padding-top: 1px; }
  .letterhead .contact-block { left: 4px; top: 655px; }
  .letterhead .brand-faint { position: absolute; right: 20px; top: 660px; font-size: 30px; }

  /* Business cards */
  .card { top: 76px; width: 232px; height: 124px; }
  .card-front { left: 619px; }
  .card-back { left: 884px; }
  .card-front .tagline { position: absolute; right: 10px; top: 10px; font-size: 8px; font-weight: 700; color: var(--navy); }
  .card-front .rule { position: absolute; right: 0; top: 24px; width: 150px; height: 2px; background: var(--navy); }
  .card-front .person { position: absolute; left: 0; top: 38px; padding-left: 8px; border-left: 3px solid var(--navy); color: var(--navy); }
  .card-front .person .who { font-size: 9px; font-weight: 700; }
  .card-front .person .role { font-size: 6px; font-weight: 500; margin-bottom: 7px; }
  .card-front .person ul { list-style: none; font-size: 5.5px; line-height: 1.7; color: var(--ink); }
  .card-front .corner { position: absolute; right: 0; bottom: 0; width: 110px; height: 44px; background: var(--navy); }
  .card-front .corner .brand { color: var(--paper); position: absolute; right: 10px; top: 14px; font-size: 16px; }
  .card-back .brand { position: absolute; left: 0; right: 0; top: 50px; text-align: center; font-size: 24px; }

  /* Envelopes */
  .envelope-back { left: 619px; top: 230px; width: 511px; height: 230px; }
  .envelope-back svg { position: absolute; left: 0; top: 0; }
  .envelope-back .brand { position: absolute; left: 0; right: 0; top: 30px; text-align: center; font-size: 26px; color: #4a6c8c; }
  .envelope-front { left: 619px; top: 495px; width: 511px; height: 251px; }
  .envelope-front .brand-main { position: absolute; left: 14px; top: 24px; font-size: 28px; }
  .envelope-front .contact-block { left: 0; top: 196px; }
  .envelope-front .brand-faint { position: absolute; right: 22px; top: 196px; font-size: 26px; }
</style>
</head>
<body>

<section class="sheet letterhead">
  <div class="brand brand-main">TESSERA</div>
  <div class="header-band"></div>
  <div class="company-title">
    <div class="name">TESSERA TILING</div>
    <div class="abn">ABN 12 345 678 901</div>
  </div>
  <div class="letter-body">
    <p>Dear Ms. Harlow:</p>
    <p>Nothing is as exciting as getting ready for game day.</p>
    <p>The players warming up, the buzz of the crowd as they enter the park, even the smell of the stadium, all make for an electrically charged atmosphere. I’ve seen it first hand, and I love it.</p>
    <p>I’ve been around professional sports since I was a child. My father worked as a National League Club scout for more than 35 years. Even more importantly, I had the pleasure of spending this past summer as an intern for the Riverton Rivets minor league baseball team.</p>
    <p>It was an amazing experience. I interned in the Public/Media Relations department and had a chance to try my hand at an incredible variety of projects. I worked with a regional sports network as they covered the play of a veteran coach and a city legends game. I handled all our player appearances. I even set up and ran our first baseball camp. I usually put in 80 hours a week and couldn’t get enough!</p>
    <p>The Rivets experience, in addition to work for a local football club and my Sports Management major, all have me extremely interested in pursuing a career as a Sports Marketing upon graduation.</p>
    <p>I would love to talk with you more about my passion, my background, and your organization. I look forward to touching base with you soon.</p>
    <p class="signoff">Regards,</p>
    <p class="signoff">Jo Marsh</p>
  </div>
  <div class="contact-block">
    <div class="marker"></div>
    <ul>
      <li>A : PO BOX 48 RIVERTON NSW 2170</li>
      <li>W : WWW.TESSERATILING.COM.AU</li>
      <li>M : 0400 555 123</li>
    </ul>
  </div>
  <div class="brand brand-faint">TESSERA</div>
</section>

<section class="sheet card card-front">
  <div class="tagline">TESSERA TILING</div>
  <div class="rule"></div>
  <div class="person">
    <div class="who">Linh Tran</div>
    <div class="role">Project Manager</div>
    <ul>
      <li>0400 555 123</li>
      <li>www.tesseratiling.com.au</li>
      <li>info@tesseratiling.com.au</li>
      <li>Fax 02 9000 0000</li>
    </ul>
  </div>
  <div class="corner"><div class="brand">TESSERA</div></div>
</section>

<section class="sheet card card-back">
  <div class="brand">TESSERA</div>
</section>

<section class="sheet envelope-back">
  <svg width="511" height="230" viewBox="0 0 511 230" aria-hidden="true">
    <polygon points="0,0 511,0 511,18 255,120 0,18" fill="var(--navy)"/>
  </svg>
  <div class="brand">TESSERA</div>
</section>

<section class="sheet envelope-front">
  <div class="brand brand-main">TESSERA</div>
  <div class="contact-block">
    <div class="marker"></div>
    <ul>
      <li>A : PO BOX 48 RIVERTON NSW 2170</li>
      <li>W : WWW.TESSERATILING.COM.AU</li>
      <li>M : 0400 555 123</li>
    </ul>
  </div>
  <div class="brand brand-faint">TESSERA</div>
</section>

</body>
</html>
```